Velvet Harbor (A luxury Travel Website)

website text attached in document below

images also attached

feel free to use other images if needed

Target Market(s)

Luxury Seekers and wealthy couples / families

Industry/Entity Type

Luxury Travel

Coding

Coded - Design and coding required

Number of Pages Required

1 page

Requirements
Must have
• A luxury design and easy use.
Nice to have
• Ease of use of page, incorporation of images into the flow of the site

```html
<!DOCTYPE html>
<html lang="en">
<head>
<meta charset="utf-8">
<title>Velvet Harbor — Luxury Travel</title>
<link href="https://fonts.googleapis.com/css2?family=Questrial&family=Nunito:wght@400;600&display=swap" rel="stylesheet">
<style>
:root{
  --ink:#000;
  --text:#111;
  --muted:#555;
  --white:#fff;
  --sky:#8ecdf0;
  --sky-soft:#eaf4fb;
  --teal:#9fd3ea;
  --line:#cfd6dc;
}
*{box-sizing:border-box;margin:0;padding:0}
html,body{width:1200px;height:2915px;overflow:hidden}
body{font-family:"Nunito",sans-serif;color:var(--text);background:var(--white);position:relative}
.heading{font-family:"Questrial",sans-serif;text-transform:uppercase;font-weight:400;letter-spacing:.5px}
.abs{position:absolute}
.brand{font-family:"Questrial",sans-serif;color:var(--teal);text-transform:uppercase;letter-spacing:2px}
.icon-ring{width:44px;height:44px;border:1.5px solid var(--teal);border-radius:50%;display:flex;align-items:center;justify-content:center}
.icon-ring svg{width:20px;height:20px;stroke:var(--teal);fill:none;stroke-width:1.6}
.contact{display:flex;align-items:center;gap:12px;color:var(--white);font-size:12.5px;line-height:1.45}
.contact .label{text-transform:uppercase;font-size:12px}
.btn{display:inline-flex;align-items:center;gap:10px;background:var(--sky);border-radius:22px;height:42px;padding:0 10px 0 22px;font-family:"Questrial",sans-serif;font-size:13px;text-transform:uppercase;color:#0d2b3d}
.btn .go{width:26px;height:26px;border-radius:50%;background:var(--ink);display:flex;align-items:center;justify-content:center}
.btn .go svg{width:10px;height:10px;stroke:var(--white);fill:none;stroke-width:2}
.field{position:absolute;height:42px;border:1px solid var(--line);background:var(--white);border-radius:3px;font-size:13px;color:#444;padding:0 21px;display:flex;align-items:center;justify-content:space-between}
.photo{position:absolute;border-radius:8px;overflow:hidden}
.photo .caption{position:absolute;left:26px;bottom:28px;color:var(--white);font-family:"Questrial",sans-serif;text-transform:uppercase;line-height:1.3}
.hotel-card{position:absolute;top:2219px;width:282px;height:306px;border:1px solid #e4e4e4;border-radius:6px;overflow:hidden}
.hotel-card .shot{height:239px}
.hotel-card .name{height:67px;display:flex;align-items:center;justify-content:center;font-family:"Questrial",sans-serif;font-size:16px;text-transform:uppercase}
</style>
</head>
<body>

<header class="abs site-header" style="left:0;top:0;width:1200px;height:88px;background:var(--ink)">
  <div class="abs brand" style="left:141px;top:24px;font-size:30px">Velvet Harbor</div>
  <div class="abs contact" style="left:860px;top:22px">
    <div class="icon-ring"><svg viewBox="0 0 24 24"><rect x="3" y="6" width="18" height="13" rx="1"/><path d="M3 7l9 7 9-7"/></svg></div>
    <div><div class="label">Email</div>info@velvetharbor.com.au</div>
  </div>
</header>

<section class="abs hero" style="left:0;top:88px;width:1200px;height:518px;background:radial-gradient(ellipse at 40% 40%,#7a5a4c 0%,#4a3029 45%,#241716 100%)" role="img" aria-label="Traveller relaxing in a business class airline seat">
  <h1 class="abs heading" style="left:0;width:1200px;top:168px;text-align:center;color:var(--white);font-size:33px;line-height:46px">Looking to stay at a star hotel or to<br>fly business class anywhere</h1>
  <p class="abs" style="left:0;width:1200px;top:270px;text-align:center;color:var(--white);font-size:14.5px;font-weight:600">Share A Screenshot of Your Travel Plans And We Beat The Price, Within 24 Hours</p>
  <div class="abs" style="left:0;width:1200px;top:308px;text-align:center"><span class="btn">Contact us today<span class="go"><svg viewBox="0 0 10 10"><path d="M3 1l4 4-4 4"/></svg></span></span></div>
</section>

<section class="abs quick-quote" style="left:0;top:606px;width:1200px;height:326px">
  <h2 class="abs heading" style="left:141px;top:73px;width:500px;font-size:25px;line-height:38px">We work directly with hotels and airlines to get you the best price,always.</h2>
  <div class="field" style="left:690px;top:84px;width:368px">Name</div>
  <div class="field" style="left:690px;top:135px;width:368px">Upload Screenshot<svg width="16" height="16" viewBox="0 0 16 16" fill="none" stroke="#222" stroke-width="1.5"><path d="M8 11V2M4.5 5.5L8 2l3.5 3.5M2 10v4h12v-4"/></svg></div>
  <div class="abs" style="left:690px;top:198px"><span class="btn">Submit now<span class="go"><svg viewBox="0 0 10 10"><path d="M3 1l4 4-4 4"/></svg></span></span></div>
</section>

<section class="abs holiday-panel" style="left:141px;top:932px;width:918px;height:459px;background:var(--sky-soft);border-radius:12px">
  <div class="photo" style="left:42px;top:46px;width:353px;height:367px;background:linear-gradient(160deg,#3d6fa3 0%,#6b8a5a 45%,#c98a43 70%,#1f5a7a 100%)" role="img" aria-label="Resort with palm trees and a lit pool at dusk"></div>
  <h2 class="abs heading" style="left:442px;top:51px;width:420px;font-size:25px;line-height:38px">Tell us about your next holiday plans. The more details the better</h2>
  <div class="field" style="left:443px;top:184px;width:212px">Name</div>
  <div class="field" style="left:664px;top:184px;width:212px">Email</div>
  <div class="field" style="left:443px;top:236px;width:212px">Phone</div>
  <div class="field" style="left:664px;top:236px;width:212px">Date</div>
  <div class="field" style="left:443px;top:289px;width:99px">Adult</div>
  <div class="field" style="left:553px;top:289px;width:99px">Child</div>
  <div class="field" style="left:664px;top:289px;width:212px">Destination</div>
  <div class="abs" style="left:443px;top:354px"><span class="btn">Submit now<span class="go"><svg viewBox="0 0 10 10"><path d="M3 1l4 4-4 4"/></svg></span></span></div>
</section>

<section class="abs destinations" style="left:0;top:1476px;width:1200px;height:602px;background:var(--ink)">
  <div class="photo" style="left:141px;top:85px;width:453px;height:430px;background:linear-gradient(180deg,#4a6f9c 0%,#8a6a4a 50%,#2f4a3a 75%,#0d2a24 100%)" role="img" aria-label="Tropical resort building reflected in a pool">
    <div class="caption" style="font-size:23px">Magna aliqm<br>erat volutpat</div>
  </div>
  <div class="photo" style="left:608px;top:85px;width:451px;height:206px;background:linear-gradient(120deg,#1d6f8a 0%,#2ea3b8 50%,#cfe3d8 80%,#2f5a32 100%)" role="img" aria-label="Aerial view of overwater villas on a turquoise lagoon">
    <div class="caption" style="font-size:23px">Tincidunt ut<br>laoreet dolore</div>
  </div>
  <div class="photo" style="left:608px;top:309px;width:218px;height:205px;background:linear-gradient(180deg,#9fb8cf 0%,#6a5a44 45%,#2a4a4a 100%)" role="img" aria-label="Modern resort pavilion beside water">
    <div class="caption" style="font-size:17px">Duis autem<br>vel eum</div>
  </div>
  <div class="photo" style="left:840px;top:309px;width:219px;height:205px;background:linear-gradient(180deg,#9cc4df 0%,#6fc8cc 40%,#7a5a44 70%,#3aa6b0 100%)" role="img" aria-label="Row of thatched overwater bungalows">
    <div class="caption" style="font-size:17px">Ut wisi enim<br>ad minim</div>
  </div>
</section>

<h2 class="abs heading" style="left:0;width:1200px;top:2152px;text-align:center;font-size:30px">Best 5 star hotels</h2>
<div class="hotel-card" style="left:141px"><div class="shot" style="background:linear-gradient(180deg,#3f7fc2 0%,#6b4a30 45%,#4f7a3a 80%,#9a9a8a 100%)" role="img" aria-label="Open-air villa with garden path and palms"></div><div class="name">Duis autem vel eum</div></div>
<div class="hotel-card" style="left:458px"><div class="shot" style="background:linear-gradient(180deg,#2a66c4 0%,#c9b8a0 45%,#5a8a4a 65%,#3fc0e0 100%)" role="img" aria-label="High-rise hotel with a large blue pool"></div><div class="name">Ut wisi enim ad minim</div></div>
<div class="hotel-card" style="left:777px"><div class="shot" style="background:linear-gradient(110deg,#5a3a22 0%,#8a5a36 40%,#d8cfc0 70%,#8fb08a 100%)" role="img" aria-label="Hotel bedroom with wood panelling and a large bed"></div><div class="name">Delenit augue dolore</div></div>

<footer class="abs site-footer" style="left:0;top:2611px;width:1200px;height:304px;background:var(--ink)">
  <div class="abs brand" style="left:0;width:1200px;top:70px;text-align:center;font-size:40px">Velvet Harbor</div>
  <div class="abs contact" style="left:267px;top:173px">
    <div class="icon-ring"><svg viewBox="0 0 24 24"><path d="M5 4h4l2 5-2.5 1.5a11 11 0 005 5L15 13l5 2v4a1 1 0 01-1 1A16 16 0 014 5a1 1 0 011-1z"/></svg></div>
    <div><div class="label">Phone</div>123-456-7890</div>
  </div>
  <div class="abs contact" style="left:476px;top:173px">
    <div class="icon-ring"><svg viewBox="0 0 24 24"><path d="M12 21s-6-6-6-11a6 6 0 0112 0c0 5-6 11-6 11z"/><circle cx="12" cy="10" r="2"/></svg></div>
    <div>123 Lorem ipsum dolor sit amet<br>consectetu adipiscing sed.</div>
  </div>
  <div class="abs contact" style="left:794px;top:173px">
    <div class="icon-ring"><svg viewBox="0 0 24 24"><rect x="3" y="6" width="18" height="13" rx="1"/><path d="M3 7l9 7 9-7"/></svg></div>
    <div><div class="label">Email</div>info@velvetharbor.com.au</div>
  </div>
  <div class="abs" style="left:141px;top:246px;width:918px;height:1px;background:#333"></div>
  <p class="abs" style="left:0;width:1200px;top:265px;text-align:center;color:var(--white);font-size:12.5px">Copyright © 2022 VelvetHarbor.com.au. All Rights Reserved.</p>
</footer>

</body>
</html>
```